I need to redesign this website. Modern Fun Professional Redesign For www.JollyPerkHub.com = New Name www.ClaimVouchly.com

Use existing content as it is on website exactly and we will revise after initial mock ups.

The new name will be ClaimVouchly.com please make a quick logo for this site too while redesigning.

Make it look like an official website....

Target Market(s)

Consumers that are redeeming certificates that businesses gave to them as a gift for customer loyalty,e tc.

Industry/Entity Type

It Professional

Logo Text

www.ClaimVouchly.com

Number of Pages Required

4 page

Colors

Designer to choose colors to be used in the design.

Requirements
Must have
• Must look professional, build trust and credibility.
Nice to have
• open
Should not have
• open

```html
<!DOCTYPE html>
<html lang="en">
<head>
<meta charset="utf-8">
<title>ClaimVouchly.com – The Redemption Source</title>
<link href="https://fonts.googleapis.com/css2?family=Roboto:wght@400;500;700&family=Source+Sans+Pro:wght@400;600;700&display=swap" rel="stylesheet">
<style>
:root{
  --navy:#0d2a3a;
  --navy-deep:#0a2230;
  --teal:#5cc2cc;
  --orange:#f26b21;
  --white:#ffffff;
  --ink:#222a30;
  --muted:#8a9096;
  --grey-bg:#e6e8ea;
  --card-text:#444b50;
}
*{margin:0;padding:0;box-sizing:border-box}
html,body{width:859px;height:1200px;overflow:hidden}
body{position:relative;font-family:"Source Sans Pro",sans-serif;background:var(--white);color:var(--ink)}
.abs{position:absolute}

/* hero */
.hero{left:0;top:0;width:859px;height:472px;background:linear-gradient(160deg,#0f4256 0%,#0d3446 45%,#0a2535 100%)}
.hero-strip{left:0;top:310px;width:859px;height:162px;background:linear-gradient(90deg,rgba(200,60,40,.35),rgba(220,210,190,.35) 18%,rgba(90,140,60,.45) 38%,rgba(13,52,70,0) 55%,rgba(220,220,215,.4) 70%,rgba(230,190,80,.4) 90%,rgba(240,240,235,.5))}
.logo{font-family:"Source Sans Pro",sans-serif}
.logo-name{font-size:24px;font-weight:700;color:var(--teal);letter-spacing:-.5px;line-height:1}
.logo-sub{font-size:10px;font-weight:600;color:var(--white);margin:2px 0 0 6px}
.nav{top:27px;left:483px;display:flex;gap:0;font-size:10px;color:var(--white);font-family:"Source Sans Pro",sans-serif}
.nav a{color:var(--white);text-decoration:none;margin-right:20px}
.nav a.active{border-bottom:1.5px solid var(--orange);padding-bottom:2px}
.nav .phone{color:var(--teal);display:flex;align-items:center;gap:4px;margin-left:-2px}
.welcome{top:124px;left:0;width:859px;text-align:center;color:var(--white)}
.welcome small{display:block;font-family:"Roboto",sans-serif;font-size:12px}
.welcome h1{font-family:"Roboto",sans-serif;font-size:24px;font-weight:700;margin-top:3px;letter-spacing:.2px}
.welcome p{font-size:12px;line-height:17px;margin-top:7px;color:#e6eef2}
.welcome p b{color:var(--teal)}
.cert-form{top:225px;left:301px;width:257px;height:43px;background:var(--white);border-radius:22px}
.cert-form span{position:absolute;left:20px;top:14px;font-size:11px;color:#9aa0a5}
.cert-go{position:absolute;right:2px;top:2px;width:39px;height:39px;border-radius:50%;background:var(--orange);color:var(--white);font-family:"Roboto",sans-serif;font-weight:700;font-size:11px;display:flex;align-items:center;justify-content:center}
.lead{top:283px;left:0;width:859px;text-align:center;color:var(--white);font-size:11px}

/* philosophy */
.goal{top:486px;left:0;width:859px;text-align:center;font-family:"Roboto",sans-serif}
.goal p{font-size:12.5px;color:var(--ink)}
.goal q{display:block;margin-top:7px;font-size:13.5px;font-weight:500;color:var(--orange);quotes:none}

/* testimonials */
.testi-bg{left:0;top:545px;width:859px;height:468px;background:linear-gradient(180deg,#eceeef 0%,#dfe2e4 55%,#e8eaeb 100%)}
.section-title{top:580px;left:80px;font-family:"Roboto",sans-serif;font-size:13.5px;font-weight:500;color:var(--ink)}
.view-more{top:583px;left:720px;font-family:"Roboto",sans-serif;font-size:9px;font-weight:500;color:#6b7176}
.card{top:617px;width:221px;height:168px;background:var(--white);box-shadow:0 1px 3px rgba(0,0,0,.08);text-align:center;padding:14px 18px 0}
.card::after{content:"";position:absolute;left:18px;bottom:-18px;border-left:0 solid transparent;border-right:18px solid transparent;border-top:18px solid var(--white)}
.card .mark{font-family:"Roboto",sans-serif;font-weight:700;font-size:30px;line-height:24px;height:22px;color:var(--teal)}
.card p{margin-top:8px;font-size:9.3px;line-height:14.7px;color:var(--card-text)}
.who{top:791px}
.who b{display:block;font-size:11px;font-weight:600;color:var(--ink)}
.who span{display:block;font-size:7.5px;line-height:12px;color:var(--muted);margin-top:2px}
.divider{top:867px;left:0;width:859px;height:1px;background:#d3d6d9}
.help{top:901px;left:0;width:859px;text-align:center;font-family:"Roboto",sans-serif;font-size:13.5px;font-weight:500;line-height:18.5px;color:var(--ink)}
.btn{top:947px;left:368px;width:123px;height:29px;border-radius:15px;background:var(--orange);color:var(--white);font-family:"Roboto",sans-serif;font-size:9px;font-weight:700;display:flex;align-items:center;justify-content:center}

/* footer */
.footer{left:0;top:1013px;width:859px;height:187px;background:var(--navy)}
.f-logo{top:1048px;left:80px}
.f-addr{top:1094px;left:80px;font-size:9px;line-height:16px;color:#8a9aa4}
.f-col{top:1047px}
.f-col h4{font-family:"Roboto",sans-serif;font-size:9px;font-weight:700;color:var(--white);margin-bottom:5px;letter-spacing:.2px}
.f-col a{display:flex;align-items:center;gap:5px;font-size:9px;line-height:16px;color:#8a9aa4;text-decoration:none}
.f-col a i{width:5px;height:5px;border-radius:50%;background:#8a9aa4;display:inline-block}
.email{top:1066px;left:618px;width:161px;height:26px;border-radius:13px;background:var(--white);font-size:9px;color:#8a9096;padding:7px 14px}
.subscribe{top:1098px;left:618px;width:161px;height:26px;border-radius:13px;background:var(--teal);color:var(--white);font-family:"Roboto",sans-serif;font-size:9px;font-weight:700;display:flex;align-items:center;justify-content:center}
.f-line{top:1162px;left:0;width:859px;height:1px;background:#173a4c}
.copy{top:1174px;left:0;width:859px;text-align:center;font-size:9px;color:#8a9aa4}
</style>
</head>
<body>

<div class="abs hero" role="img" aria-label="Dark teal photo of a traveller on a scenic lookout"></div>
<div class="abs hero-strip" role="img" aria-label="Row of reward products: fuel nozzle, wine bottles, vegetable basket, music player, tablet and a plated meal"></div>

<div class="abs logo" style="top:18px;left:80px">
  <div class="logo-name">ClaimVouchly</div>
  <div class="logo-sub">Redemption Processing Center</div>
</div>

<nav class="abs nav">
  <a class="active">Home</a><a>Contact Us</a><a>Testimonials</a><a>Terms</a>
  <span class="phone"><svg width="7" height="10" viewBox="0 0 7 10"><rect x=".5" y=".5" width="6" height="9" rx="1" fill="none" stroke="#5cc2cc"/><rect x="1.5" y="1.8" width="4" height="5" fill="#5cc2cc"/></svg>1800 555 0142</span>
</nav>

<div class="abs welcome">
  <small>WELCOME TO</small>
  <h1>THE REDEMPTION SOURCE</h1>
  <p>Please Enter A Valid <b>Certificate ID</b> In The Form Below<br>To Redeem Your Certificate And To View Faq's, Terms And Locations.</p>
</div>

<div class="abs cert-form"><span>Enter Certificate ID</span><div class="cert-go">GO</div></div>
<div class="abs lead">ClaimVouchly.com is a leading company in travel certificate fulfillment.</div>

<div class="abs goal">
  <p>Our goal is to make it easy for you to redeem your certificate and our philosophy is this:</p>
  <q>"What good is it to receive a gift certificate if you can't use it?".</q>
</div>

<div class="abs testi-bg" role="img" aria-label="Faded photo of a couple sitting on a seaside boardwalk"></div>
<h2 class="abs section-title">TESTIMONIALS</h2>
<div class="abs view-more">VIEW MORE ▸</div>

<div class="abs card" style="left:80px"><div class="mark">“</div><p>"My vacation was excellent! We started in Milano, and visited the Duomo Cathedral; then we went to Lako Como, and then proceeded to Sorrento; Amalfi; Positano; Bari and ended in the Abbruzzi area. Wonderful people, weather, great food and great wine!"</p></div>
<div class="abs card" style="left:319px"><div class="mark">“</div><p>"I am extremely happy with my service, everything worked out perfect. My wife and I had a great time in Las Vegas. The hotel we stayed at was very nice and clean. I would go there again. Thank you for everything."</p></div>
<div class="abs card" style="left:558px"><div class="mark">“</div><p>"My vacation was excellent. The photo I have enclosed is the view I saw from my lovely room when I enjoyed Las Vegas with a friend last November! The weather was perfect. The entertainment options were outstanding!"</p></div>

<div class="abs who" style="left:120px"><b>Clara M.</b><span>Port Orange, FL<br>Added on 10/12/2015 11:22:28 am</span></div>
<div class="abs who" style="left:359px"><b>Mateo R.</b><span>Van Nuys, CA<br>Added on 09/24/2015 02:32:30 pm</span></div>
<div class="abs who" style="left:598px"><b>Helen T.</b><span>Austin Texas<br>Added on 09/24/2015 02:30:19 pm</span></div>

<div class="abs divider"></div>
<div class="abs help">If you have any questions about how to redeem a certain certificate,<br>please contact us. We are here to help.</div>
<div class="abs btn">CONTACT US TODAY!</div>

<footer class="abs footer"></footer>
<div class="abs logo f-logo">
  <div class="logo-name">ClaimVouchly</div>
  <div class="logo-sub">Redemption Processing Center</div>
</div>
<div class="abs f-addr">The Redemption Center<br>4120 Harbor View Rd Ste B #210<br>Linden Park, Ca 91877</div>

<div class="abs f-col" style="left:259px"><h4>QUICK LINKS</h4><a>Home</a><a>Contact Us</a><a>Testimonials</a><a>Terms</a></div>
<div class="abs f-col" style="left:379px"><h4>INFORMATION</h4><a>Terms of Use</a><a>Privacy</a><a>Sitemap</a></div>
<div class="abs f-col" style="left:498px"><h4>WE'RE SOCIAL</h4><a><i></i>Chatterly</a><a><i></i>Tweetline</a><a><i></i>Linkwork</a></div>
<div class="abs f-col" style="left:618px"><h4>SUBSCRIBE NEWSLETTER</h4></div>
<div class="abs email">Email Address</div>
<div class="abs subscribe">SUBSCRIBE NOW!</div>

<div class="abs f-line"></div>
<div class="abs copy">©2017 ClaimVouchly. All Rights Reserved</div>

</body>
</html>
```